Business Card Design and Logo Needed

I need Business Cards and a Logo for my website and public speaking business which can be found at: www.talia-ferrow.com

I'm looking for creative and unique ideas. Some business cards I've found online that I like can be found at:
http://gigmarketloft.com/general/18-smokin-hot-business-card-designs/

and at

http://www.theprintnookery.com/2009/04/50-creative-business-cards-of-50-graphic-designers/

```html
<!DOCTYPE html>
<html lang="en">
<head>
<meta charset="utf-8">
<title>Talia Ferrow — Business Card</title>
<link rel="stylesheet" href="https://fonts.googleapis.com/css2?family=Michroma&family=Quicksand:wght@400&display=swap">
<style>
  :root {
    --page: #ffffff;
    --card-top: #6f2519;
    --card-bottom: #4a1410;
    --emblem: rgba(255, 255, 255, 0.16);
    --name: #ffffff;
    --role: #b8352f;
    --contact: #d8a698;
  }
  html, body {
    margin: 0;
    padding: 0;
    width: 1200px;
    height: 325px;
    overflow: hidden;
    background: var(--page);
  }
  .canvas {
    display: block;
    width: 1200px;
    height: 325px;
  }
  .stop-top { stop-color: var(--card-top); }
  .stop-bottom { stop-color: var(--card-bottom); }
  .emblem { fill: var(--emblem); }
  .card-name {
    font-family: "Quicksand", sans-serif;
    font-size: 30px;
    fill: var(--name);
  }
  .emblem-name {
    font-family: "Quicksand", sans-serif;
    font-size: 11px;
    fill: var(--name);
    opacity: 0.75;
  }
  .role, .contact {
    font-family: "Michroma", sans-serif;
    font-size: 10.5px;
    letter-spacing: 1.2px;
  }
  .role { fill: var(--role); }
  .contact { fill: var(--contact); }
</style>
</head>
<body>
<svg class="canvas" viewBox="0 0 1200 325" xmlns="http://www.w3.org/2000/svg">
  <defs>
    <linearGradient id="card-fill" x1="0" y1="0" x2="0" y2="1">
      <stop offset="0" class="stop-top"/>
      <stop offset="1" class="stop-bottom"/>
    </linearGradient>
  </defs>

  <!-- Front -->
  <g class="card-front">
    <path role="img" aria-label="Deep red card face with a subtle checkered texture"
          fill="url(#card-fill)"
          d="M186 33 H557 V232 A80 80 0 0 1 477 312 H111 V108 A75 75 0 0 1 186 33 Z"/>
    <circle class="emblem" cx="331" cy="173" r="82"/>
    <text class="card-name" x="239" y="233">Talia Ferrow</text>
  </g>

  <!-- Back -->
  <g class="card-back">
    <path role="img" aria-label="Deep red card face with a subtle checkered texture"
          fill="url(#card-fill)"
          d="M635 33 H1005 A75 75 0 0 1 1080 108 V312 H710 A75 75 0 0 1 635 237 Z"/>
    <circle class="emblem" cx="1010" cy="106" r="45"/>
    <text class="emblem-name" x="1010" y="110" text-anchor="middle">Talia Ferrow</text>

    <text class="role" x="659" y="226">MOTIVATIONAL SPEAKER</text>
    <text class="role" x="659" y="250">PHILANTHROPIST</text>
    <text class="role" x="659" y="275">AUTHOR</text>

    <text class="contact" x="1056" y="226" text-anchor="end">MOB : 0198 765432</text>
    <text class="contact" x="1056" y="252" text-anchor="end">WWW.TALIAFERROW.COM</text>
    <text class="contact" x="1056" y="275" text-anchor="end">TALIAFERROW@MAILBOX.COM</text>
  </g>
</svg>
</body>
</html>
```